The Velmora Company Sweet Packaging Design

The Velmora Trading Company is looking for a logo and label design for an upcoming line of honey based health and beauty products that are sourced from the Polynesian Islands (Hawaii, New Zealand, Fiji etc.).The brand will be premium price positioned and the design and packaging should exude class and quality.The design should be flexible enough to add products from future locations.We would like to see the design across three different product forms:1. Glass Honey Jar (main product)2. Hand cream / lotion (pump bottle, or lotion tube)3. Small box (e.g. throat lozenges / gum packet etc.)The Polynesia Islands are unique and exotic locations; the design/packaging should reflect this but should not be overly complicated. Each individual island has their own distinct culture and history but they have many commonalities which fall under "Polynesian Culture". The Velmora Trading Company is an umbrella brand that should be able to support a growing number of products.Possible designs may (but are not required to) incorporate local flowers (Hawaii / Hibiscus flower, New Zealand / Manuka Flower etc.) into the design, Islands, and boutique feel (elegant classy looking)Please feel free to ask more questions for further guidance but we really want to see where the creative process can take us outside of what we have already considered internally.
Updates

We needed to modify our idea slightly because of competition.

We needed extend to get a few more ideas. We did not want to copy our competition and needed to add a part to our design that we did not include before.

Target Market(s)

Health conscious people. Honey lovers.

Font styles to use
Serif
Sans Serif
Decorative

Colors

Designer to choose colors to be used in the design.

Requirements
Must have
• a little tribal look. because its 100% polynesian Honey.. it would be nice to have the fee of that in the design..

```html
<!DOCTYPE html>
<html lang="en">
<head>
<meta charset="utf-8">
<title>The Velmora Trading Company – Candy Label</title>
<link href="https://fonts.googleapis.com/css2?family=Oswald:wght@600&family=Courgette&display=swap" rel="stylesheet">
<style>
  :root {
    --page: #ffffff;
    --ink: #000000;
    --cream: #f6ecd2;
    --floral-mid: #8a7f66;
    --floral-dark: #14120e;
    --honey: #efb320;
    --olive-gold: #b4ab2c;
    --gold-text: #f5b50c;
  }
  html, body {
    margin: 0;
    padding: 0;
    width: 1059px;
    height: 1200px;
    overflow: hidden;
    background: var(--page);
  }
  .canvas {
    position: relative;
    width: 1059px;
    height: 1200px;
  }
  .label {
    position: absolute;
    left: 42px;
    top: 90px;
    width: 975px;
    height: 1020px;
  }
  .label-art {
    position: absolute;
    inset: 0;
    width: 975px;
    height: 1020px;
  }
  .brand-block {
    position: absolute;
    left: 191px;
    width: 600px;
    top: 468px;
    text-align: center;
  }
  .brand-name {
    margin: 0;
    font-family: "Oswald", sans-serif;
    font-weight: 600;
    font-size: 58px;
    line-height: 1.1;
    letter-spacing: 3px;
    color: var(--gold-text);
    text-transform: uppercase;
  }
  .product-name {
    margin: 40px 0 0;
    font-family: "Courgette", cursive;
    font-size: 66px;
    line-height: 1;
    color: var(--gold-text);
  }
</style>
</head>
<body>
  <main class="canvas">
    <section class="label">
      <svg class="label-art" viewBox="0 0 975 1020" xmlns="http://www.w3.org/2000/svg">
        <defs>
          <radialGradient id="floral-tone" cx="0.5" cy="0.45" r="0.75">
            <stop offset="0" stop-color="var(--floral-mid)"/>
            <stop offset="0.55" stop-color="#4a4436"/>
            <stop offset="1" stop-color="var(--floral-dark)"/>
          </radialGradient>
        </defs>
        <path class="floral-field" role="img" aria-label="Repeating cream hibiscus flower pattern on a black ground"
              d="M0 150 Q487 -20 975 150 L975 505 L0 505 Z" fill="url(#floral-tone)"/>
        <path class="honey-band" d="M0 500 L975 500 L975 985 Q487 1050 0 985 Z" fill="var(--honey)"/>
        <polygon class="hex-frame" points="277,225 702,225 922,585 702,945 277,945 60,585" fill="var(--olive-gold)"/>
        <polygon class="hex-panel" points="285,238 694,238 906,585 694,932 285,932 74,585" fill="var(--ink)"/>
        <circle class="seal-ring" cx="491" cy="592" r="296" fill="none" stroke="var(--olive-gold)" stroke-width="11"/>
      </svg>
      <div class="brand-block">
        <h1 class="brand-name">The Velmora<br>Trading<br>Company</h1>
        <p class="product-name">Candy</p>
      </div>
    </section>
  </main>
</body>
</html>
```